Forensic Psychology and Polygraph Needs Clever Catchy Logo

There's a massive trade show coming up and we are looking to debut a new, clever logo for our business cards. We are a private practice that offers psychological evaluations, therapeutic counseling, and polygraphing. Our website is ketvorin.com (to get a better idea of the color scheme) and instead of the nature/cuddly image that other psychology organizations like to go for, we are interested in cultivating a business, strength, and professional image.
Attached are some popular logos and designs to get those creative juices flowing! I would like to avoid the brain/psi logo as this has been to death so bonus points definitely for originality.
Target Market(s)
governmental agencies, third party mental health providers, individual private pay clients
Industry/Entity Type
Mental Health
Contact Information for Business Card
One one side will be the logo and company name while on the back will be contact information and provider details (name, position, etc)
Look and feel

```html
<!DOCTYPE html>
<html lang="en">
<head>
<meta charset="utf-8">
<title>Halvern &amp; Associates — Business Card</title>
<link href="https://fonts.googleapis.com/css2?family=Montserrat:wght@700&family=Open+Sans:wght@400&family=Pinyon+Script&display=swap" rel="stylesheet">
<style>
  :root {
    --page-bg: #ecebea;
    --plum-dark: #564b5c;
    --plum-light: #6e6374;
    --teal: #2bb5b0;
    --ink: #5a5a5a;
    --ink-soft: #7a7a7a;
    --card-white: #ffffff;
    --tagline: #d9d4dc;
  }
  * { margin: 0; padding: 0; box-sizing: border-box; }
  html, body {
    width: 1200px;
    height: 1200px;
    overflow: hidden;
    background: var(--page-bg);
  }
  .canvas {
    width: 1200px;
    height: 1200px;
    display: flex;
    flex-direction: column;
    align-items: center;
    justify-content: center;
    gap: 80px;
  }
  .card {
    width: 700px;
    height: 400px;
    box-shadow: 0 6px 18px rgba(0,0,0,0.12);
    position: relative;
  }

  /* Front: company name */
  .card-front {
    background: linear-gradient(135deg, var(--plum-dark) 0%, var(--plum-light) 100%);
    display: flex;
    align-items: center;
    justify-content: center;
  }
  .brand {
    text-align: right;
  }
  .brand-name {
    font-family: "Montserrat", sans-serif;
    font-weight: 700;
    font-size: 40px;
    letter-spacing: 0.5px;
    color: var(--card-white);
  }
  .brand-tagline {
    margin-top: 6px;
    font-family: "Open Sans", sans-serif;
    font-weight: 400;
    font-size: 20px;
    letter-spacing: 1px;
    color: var(--tagline);
  }

  /* Back: contact details */
  .card-back {
    background: var(--card-white);
  }
  .card-frame {
    position: absolute;
    inset: 16px;
    border: 2px solid var(--teal);
    display: flex;
    flex-direction: column;
    align-items: center;
    padding-top: 34px;
    font-family: "Open Sans", sans-serif;
    color: var(--ink);
    text-align: center;
  }
  .person-name {
    font-family: "Pinyon Script", cursive;
    font-size: 64px;
    line-height: 1;
    color: var(--teal);
  }
  .person-title {
    margin-top: 6px;
    font-size: 16px;
    color: var(--ink-soft);
  }
  .contact-line {
    font-size: 17px;
    letter-spacing: 0.4px;
  }
  .contact-phone { margin-top: 20px; }
  .contact-web { margin-top: 6px; }
  .divider {
    margin: 16px 0;
    display: block;
  }
  .address-line {
    font-size: 17px;
    letter-spacing: 0.4px;
    line-height: 1.6;
  }
</style>
</head>
<body>
  <main class="canvas">
    <section class="card card-front">
      <div class="brand">
        <div class="brand-name">Halvern &amp; Associates</div>
        <div class="brand-tagline">Psychological Services</div>
      </div>
    </section>

    <section class="card card-back">
      <div class="card-frame">
        <div class="person-name">Daniel Marsh</div>
        <div class="person-title">Director</div>
        <div class="contact-line contact-phone">555.014.2287</div>
        <div class="contact-line contact-web">www.ketvorin.com | contact@ketvorin.com</div>
        <svg class="divider" width="380" height="2" viewBox="0 0 380 2" aria-hidden="true">
          <line x1="0" y1="1" x2="380" y2="1" stroke="var(--teal)" stroke-width="1.5"/>
        </svg>
        <div class="address-line">2870 W. Cedar Ridge Rd.</div>
        <div class="address-line">Suites 204 and 208. Tempe, Arizona 85281</div>
      </div>
    </section>
  </main>
</body>
</html>
```